Transfer Tortoise - Cloud Based Data Migration Service for IT Professionals

We are looking for a smart clean website design for an informational site about our services and as a main portal into the service itself. We would like the design completed in WORDPRESS so that it will easily connect with the service.

Transfer Tortoise is a cloud based migration service providing (to start with) a online migration tool that we migrate Kelvarn Postbox mailboxes (email) with all the settings, attachments from one system to another.
The service is aimed at IT professionals, IT companies and IT departments so our customers will be very technology based.

The Service -
IT companies currently migrate email; data and databases. using a very time intensive process which is both expensive and means their customer potentially losses access to its IT for a significant period of time. Additionally there are risks with regards to compatibility between systems and loss of data.
Potential benefits include;
• cost savings
• improved customer service, including reduced downtime
• improved resilience of the process
We are therefore developing cloud based migration software/website which will automate the process, mitigating these issues, as well as providing additional benefits such as the ability to sort and migrate only certain areas of data or certain emails, to check the integrity of the data/emails moved and to also repair corrupted data and emails.
The system will effectively duplicate the data and emails onto the new system over the weeks prior to the completion date. This will enable the IT Company to complete a final synchronisation and then immediately switch over to the new system with no interruption to the end users.
There is also an added benefit that the end users can test the system (with their own data and emails) prior to the switch over date to ensure everything is in place and databases work correctly.
The system will be completely cloud based and therefore easy for the IT Companies to access. They will be able to purchase the use of the system using CoinDrift or credit card and will only need to purchase what they need, this will allow even small local IT companies the facilities which previously would have been cost prohibitive to them.

Some of the sites we like for reference are -
Trellward, brightlots, the sky shuttler.

We already have a logo design see attached and the website will need to work with this design.
Please message me if you have any questions
We do have the logo in other file formats if required.
Many Thanks

Target Market(s)

IT Sector

Industry/Entity Type

It Service

Number of Pages Required

5+ page

Requirements
Must have
• Front Page
• About Us
• Contact Info
• Blog
• Benefits
• More Information
• Must be Mobile Phone Compatible/friendly
• Log in (button) and support button on all pages (possibley top right)

```html
<!DOCTYPE html>
<html lang="en">
<head>
<meta charset="utf-8">
<title>Transfer Tortoise – Cloud Based Migration Service</title>
<link rel="stylesheet" href="https://fonts.googleapis.com/css2?family=Lato:ital,wght@0,400;0,700;1,400&family=Michroma&display=swap">
<style>
:root{
  --blue:#0aa3d8;
  --blue-dark:#0a86b8;
  --ink:#222;
  --text:#444;
  --grey-band:#d4d4d4;
  --card:#e9e9e9;
  --hero:#1b1b1b;
  --foot:#221e1b;
  --foot-deep:#1a1614;
  --news:#343231;
  --white:#fff;
}
*{box-sizing:border-box;margin:0;padding:0}
html,body{width:705px;height:1200px;overflow:hidden}
body{position:relative;font-family:'Lato',sans-serif;color:var(--text);background:var(--white)}
.abs{position:absolute}
.display{font-family:'Michroma',sans-serif;letter-spacing:2px;color:var(--ink)}

/* header */
.header{left:0;top:0;width:705px;height:90px;background:linear-gradient(#fff,#f2f2f2)}
.brand{left:70px;top:22px;display:flex;align-items:center;gap:8px}
.brand-mark{width:26px;height:26px;border-radius:50%;background:var(--blue)}
.brand-name{font-weight:700;font-size:15px;line-height:17px;color:var(--ink);letter-spacing:1.5px;width:110px}
.call-label{left:388px;top:15px;font-size:12px;color:var(--blue)}
.call-number{left:386px;top:31px;font-size:13px;color:#333;display:flex;align-items:center;gap:6px;letter-spacing:.5px}
.call-icon{width:15px;height:15px;border-radius:50%;background:#555;display:flex;align-items:center;justify-content:center}
.btn-login{left:520px;top:29px;width:52px;height:19px;background:var(--blue);color:#fff;font-size:8.5px;font-weight:700;display:flex;align-items:center;justify-content:center;gap:4px}
.btn-support{left:566px;top:29px;width:62px;height:19px;background:#2b2b2b;color:#fff;font-size:8.5px;font-weight:700;display:flex;align-items:center;justify-content:center;clip-path:polygon(8% 0,100% 0,100% 100%,0 100%)}
.nav{left:208px;top:65px;width:497px;height:25px;background:var(--blue);clip-path:polygon(3% 0,100% 0,100% 100%,0 100%)}
.nav a{position:absolute;top:7px;font-size:9px;color:#fff;text-decoration:none}
.nav a.active{font-weight:700;border-bottom:2px solid #fff;padding-bottom:2px}

/* hero */
.hero{left:0;top:90px;width:705px;height:277px;background:radial-gradient(circle at 55% 60%,#3a3a3a,var(--hero) 70%)}
.hero-title{left:78px;top:98px;font-size:20px;line-height:30px;color:#fff;font-weight:400;text-shadow:0 1px 2px #000}
.hero-art{left:300px;top:10px;width:330px;height:250px;border-radius:12px;background:radial-gradient(ellipse at 50% 50%,#4e8fc0 0%,#2a3b4a 55%,transparent 80%)}
.hero-arrow{top:85px}

/* welcome */
.welcome-title{left:0;top:398px;width:705px;text-align:center;font-size:11.5px}
.rule{height:1px;background:#bbb}
.welcome-text{left:85px;top:421px;width:535px;text-align:center;font-size:8.6px;line-height:13.5px;color:#333}
.btn-more{left:319px;top:474px;width:66px;height:19px;background:var(--blue-dark);color:#fff;font-size:8.5px;font-weight:700;display:flex;align-items:center;justify-content:center}

/* benefits */
.benefits{left:0;top:516px;width:705px;height:270px;background:radial-gradient(ellipse at 50% 30%,#e2e2e2,var(--grey-band) 80%)}
.benefits-title{left:0;top:21px;width:705px;text-align:center;font-size:11.5px}
.card{top:57px;width:165px;height:183px;background:var(--card);box-shadow:0 8px 8px -6px rgba(0,0,0,.35);text-align:center}
.card-photo{margin:6px 6px 0;height:93px}
.card h3{margin-top:11px;font-size:11px;font-weight:400;color:var(--blue)}
.card p{margin-top:5px;font-size:8.4px;line-height:13px;color:#444;padding:0 8px}
.card .more{margin-top:6px;font-size:8.5px;color:var(--blue)}

/* blog & testimonials */
.section-head{font-size:11px}
.head-rule{height:1px;background:#999;width:255px}
.post{left:77px;width:255px}
.post-thumb{left:0;top:0;width:58px;height:42px;border:2px solid #fff;box-shadow:0 0 2px #999}
.post h4{left:68px;top:0;font-size:8.2px;font-weight:400;color:#111}
.post .date{left:68px;top:12px;font-size:6.6px;color:var(--blue);font-weight:700}
.post p{left:68px;top:23px;width:185px;font-size:7.4px;line-height:11.5px;color:#333}
.dotted{left:77px;top:909px;width:255px;border-top:1px dotted #999}
.avatar{width:48px;height:48px;border-radius:50%;box-shadow:0 5px 6px -3px rgba(0,0,0,.4)}
.quote{width:180px;font-size:8.4px;line-height:13px;font-style:italic;color:#555}
.quote b{font-size:18px;color:#ccc;font-style:normal;position:absolute;left:-22px;top:-5px}
.client{font-size:8.4px;color:var(--blue)}

/* footer */
.footer-top{left:0;top:1011px;width:705px;height:107px;background:var(--foot)}
.news{left:77px;top:1011px;width:171px;height:107px;background:var(--news);padding:14px 13px}
.news h5{font-size:8.6px;color:#fff;font-weight:400;letter-spacing:.4px}
.news p{margin-top:5px;font-size:8px;color:#ddd}
.news .field{margin-top:8px;height:19px;background:#fff;font-size:6.4px;color:#333;display:flex;align-items:center;padding-left:6px;gap:5px}
.news .btn{margin-top:8px;width:57px;height:18px;background:var(--blue);color:#fff;font-size:7px;font-weight:700;display:flex;align-items:center;justify-content:center}
.info h6{font-size:9.6px;font-weight:400;color:#fff;display:flex;align-items:center;gap:6px}
.info p{margin-top:6px;font-size:7.4px;line-height:12.5px;color:#ddd}
.footer-bottom{left:0;top:1118px;width:705px;height:82px;background:var(--foot-deep)}
.foot-links a{position:absolute;top:20px;font-size:8px;color:#fff;text-decoration:none;font-weight:700}
.copyright{left:78px;top:49px;font-size:8.4px;color:#ddd}
.social{top:29px;width:28px;height:28px;border-radius:2px}
</style>
</head>
<body>

<header class="abs header">
  <div class="abs brand"><span class="brand-mark"></span><span class="brand-name">TRANSFER TORTOISE</span></div>
  <div class="abs call-label">Call us :</div>
  <div class="abs call-number"><span class="call-icon"><svg width="9" height="9" viewBox="0 0 24 24"><path fill="#fff" d="M6.6 10.8a15 15 0 006.6 6.6l2.2-2.2a1 1 0 011-.25 11.4 11.4 0 003.6.57 1 1 0 011 1V20a1 1 0 01-1 1A17 17 0 013 4a1 1 0 011-1h3.5a1 1 0 011 1 11.4 11.4 0 00.57 3.6 1 1 0 01-.25 1z"/></svg></span>(555) 0142 7788</div>
  <div class="abs btn-login"><svg width="8" height="8" viewBox="0 0 10 10"><circle cx="5" cy="3" r="2.3" fill="#fff"/><path d="M1 10a4 4 0 018 0z" fill="#fff"/></svg>Log in</div>
  <div class="abs btn-support">Support</div>
  <nav class="abs nav">
    <a class="active" href="#" style="left:25px">Home</a>
    <a href="#" style="left:82px">About Us</a>
    <a href="#" style="left:153px">Blog</a>
    <a href="#" style="left:204px">Benefits</a>
    <a href="#" style="left:270px">More Information</a>
    <a href="#" style="left:375px">Contact Us</a>
  </nav>
</header>

<section class="abs hero">
  <div class="abs hero-art" role="img" aria-label="Illustration of a cloud linked by blue cables to a laptop, desktop computers and a phone"></div>
  <h1 class="abs hero-title">We are a Providing a Online<br>&nbsp;Cloud Based Migration<br>Service</h1>
  <svg class="abs hero-arrow" style="left:38px" width="16" height="30" viewBox="0 0 16 30"><path d="M14 2L3 15l11 13" stroke="#aaa" stroke-width="2" fill="none"/></svg>
  <svg class="abs hero-arrow" style="left:651px" width="16" height="30" viewBox="0 0 16 30"><path d="M2 2l11 13L2 28" stroke="#aaa" stroke-width="2" fill="none"/></svg>
</section>

<section>
  <div class="abs rule" style="left:178px;top:405px;width:65px"></div>
  <div class="abs rule" style="left:540px;top:405px;width:65px"></div>
  <h2 class="abs display welcome-title">WELCOME TO TRANSFER TORTOISE</h2>
  <p class="abs welcome-text">Lorem ipsum dolor sit amet, consectetuer adipiscing elit, sed diam nonummy nibh euismod tincidunt ut laoreet dolore magna aliquam erat volutpat. Ut wisi enim ad minim veniam, quis nostrud exerci tation ullamcorper suscipit lobortis nisl ut aliquip ex ea commodo consequat. Duis autem vel eum iriure dolor in hendrerit in vulputate velit esse molestie consequat,</p>
  <div class="abs btn-more">Read More ▸</div>
</section>

<section class="abs benefits">
  <h2 class="abs display benefits-title">OUR BENEFITS</h2>
  <div class="abs card" style="left:77px">
    <div class="card-photo" role="img" aria-label="Photo of a hand stacking coins" style="background:linear-gradient(135deg,#f5efe8,#d8b98c)"></div>
    <h3>Cost Savings</h3>
    <p>Lorem ipsum dolor sit amet, consecte tuer adipiscing elit, sed diam</p>
    <div class="more">[+]</div>
  </div>
  <div class="abs card" style="left:270px">
    <div class="card-photo" role="img" aria-label="Photo of a support agent wearing a headset" style="background:linear-gradient(135deg,#c9cdd2,#8c7a6e)"></div>
    <h3>Improved Customer Service</h3>
    <p>Lorem ipsum dolor sit amet, consecte tuer adipiscing elit, sed diam</p>
    <div class="more">[+]</div>
  </div>
  <div class="abs card" style="left:463px">
    <div class="card-photo" role="img" aria-label="Photo of colleagues working at a laptop" style="background:linear-gradient(135deg,#dfe6ee,#5d7fa8)"></div>
    <h3>improved resilience</h3>
    <p>Lorem ipsum dolor sit amet, consecte tuer adipiscing elit, sed diam</p>
    <div class="more">[+]</div>
  </div>
</section>

<section>
  <h2 class="abs display section-head" style="left:78px;top:806px">LATEST BLOG</h2>
  <div class="abs head-rule" style="left:77px;top:827px"></div>
  <article class="abs post" style="top:839px">
    <div class="abs post-thumb" role="img" aria-label="Portrait photo of the post author" style="background:linear-gradient(135deg,#e6e0d8,#b89a80)"></div>
    <h4 class="abs">CONSECTETUER ADIPISCING</h4>
    <div class="abs date">January 18, 2016 - 3:00-4:00pm</div>
    <p class="abs">Duis autem vel eum iriure dolsed di nonumy nibhr euismod tincdunt ut laoreet dolore ma aliqed dili nonummy nibhr euismod tincidunt</p>
  </article>
  <div class="abs dotted"></div>
  <article class="abs post" style="top:927px">
    <div class="abs post-thumb" role="img" aria-label="Portrait photo of the post author" style="background:linear-gradient(135deg,#dde3ea,#4a4f5a)"></div>
    <h4 class="abs">DUIS AUTEM VELEUM IRIURE DOLSEI</h4>
    <div class="abs date">January 18, 2016 - 3:00-4:00pm</div>
    <p class="abs">Duis autem vel eum iriure dolsed di nonumy nibhr euismod tincdunt ut laoreet dolore ma aliqed dili nonummy nibhr euismod tincidunt</p>
  </article>

  <h2 class="abs display section-head" style="left:372px;top:806px">CLIENT TESTIMONIALS</h2>
  <div class="abs head-rule" style="left:372px;top:827px"></div>
  <div class="abs avatar" role="img" aria-label="Portrait photo of client" style="left:375px;top:843px;background:radial-gradient(#d9a57f,#7a4a2c)"></div>
  <p class="abs quote" style="left:468px;top:846px"><b>“</b>Lorem ipsum dolor sit amet, consectetuer adipiscing elit, sed diam nonummy nibh</p>
  <div class="abs client" style="left:469px;top:891px">Miss . Lena Marlow</div>
  <div class="abs avatar" role="img" aria-label="Portrait photo of client" style="left:374px;top:928px;background:radial-gradient(#e6e6e6,#8a8a8a)"></div>
  <p class="abs quote" style="left:468px;top:935px"><b>“</b>Lorem ipsum dolor sit amet, consectetuer adipiscing elit, sed diam nonummy nibh</p>
  <div class="abs client" style="left:470px;top:980px">Mr. Oren Vale</div>
</section>

<footer>
  <div class="abs footer-top"></div>
  <div class="abs news">
    <h5>NEWSLETTER SIGN UP</h5>
    <p>Lorem ipsum dolor sit ame venia</p>
    <div class="field"><svg width="9" height="7" viewBox="0 0 9 7"><rect x=".5" y=".5" width="8" height="6" fill="none" stroke="#333"/><path d="M.5.5l4 3 4-3" stroke="#333" fill="none"/></svg>Enter Your Email</div>
    <div class="btn">SUBSCRIBE</div>
  </div>
  <div class="abs info" style="left:262px;top:1031px">
    <h6><svg width="11" height="13" viewBox="0 0 11 13"><path d="M5.5 12S1 7.5 1 5a4.5 4.5 0 019 0c0 2.5-4.5 7-4.5 7z" fill="none" stroke="#fff"/><circle cx="5.5" cy="5" r="1.5" fill="none" stroke="#fff"/></svg>Transfer Tortoise</h6>
    <p style="margin-left:18px;width:105px">ipsum dolor sit amet, consectetuer adi piscing sed diam nonummy. 1685</p>
  </div>
  <div class="abs info" style="left:392px;top:1031px">
    <h6><svg width="12" height="12" viewBox="0 0 24 24"><path fill="none" stroke="#fff" stroke-width="1.8" d="M6.6 10.8a15 15 0 006.6 6.6l2.2-2.2a1 1 0 011-.25 11.4 11.4 0 003.6.57 1 1 0 011 1V20a1 1 0 01-1 1A17 17 0 013 4a1 1 0 011-1h3.5a1 1 0 011 1 11.4 11.4 0 00.57 3.6 1 1 0 01-.25 1z"/></svg>Phone Number</h6>
    <p style="margin-left:20px">(555) 014 2778<br>(555) 014 - 2779</p>
  </div>
  <div class="abs info" style="left:501px;top:1031px">
    <h6><svg width="13" height="10" viewBox="0 0 13 10"><rect x=".5" y=".5" width="12" height="9" fill="none" stroke="#fff"/><path d="M.5.5l6 5 6-5" stroke="#fff" fill="none"/></svg>Email Address</h6>
    <p style="margin-left:21px">info@TransferTortoise.com</p>
  </div>

  <div class="abs footer-bottom">
    <div class="foot-links">
      <a href="#" style="left:78px">Home</a>
      <a href="#" style="left:122px">About Us</a>
      <a href="#" style="left:179px">Blog</a>
      <a href="#" style="left:218px">Benefits</a>
      <a href="#" style="left:271px">More Information</a>
      <a href="#" style="left:361px">Contact Us</a>
    </div>
    <div class="abs copyright">© 2016 Transfer Tortoise. All Rights Reserved.</div>
    <div class="abs social" aria-label="Social profile" style="left:484px;background:#3b5b9a"></div>
    <div class="abs social" aria-label="Social profile" style="left:523px;background:#1ba9e0"></div>
    <div class="abs social" aria-label="Social profile" style="left:562px;background:#c9302c"></div>
    <div class="abs social" aria-label="Social profile" style="left:600px;background:#f0901e"></div>
  </div>
</footer>

</body>
</html>
```